Buch-/E-Book-Cover für einen historischen Romanen
Zielgruppe
Ich bin Autor von historischen Romanen, die Zielgruppe ist 60 % weiblich interssiert an Geschichte, Romantik, Abenteur. Es muss ein Cover designt werden, dass sowohl für E-Books als auch für Print Edtionen passt, inclusive Rücken und Einband.
Aufgabenstellung
Es sollte nicht zu kitschig werden, viele Romancover locken mit halbnackten Helden, das sollte vermieden werden. Das Buch spielt im 17. Jahrhundert, es geht um mysteriöse Todesfälle, ein Schloss, und um eine Liebesgschichte um diesen Hintergrund. Es muss en ISBN Code auf dem Rûcken eingefügt werden, Seitenzahl und genaue Abmessungen werden nach Ende Lektrorat festgelegt. Als Inspiration bitte Bücher des Autors Jonas Brenkert auf Lesotal.DE und Lesotal.UK anschauen. Dieses Buc hat jedoch andere Protagonisten und kann abweichen.

```html
<!DOCTYPE html>
<html lang="de">
<head>
<meta charset="utf-8">
<title>Das Tödliche Erbe von Schloss Rothenburg – Umschlag</title>
<link rel="stylesheet" href="https://fonts.googleapis.com/css2?family=EB+Garamond:wght@400&family=Playfair+Display:wght@400;700&family=Barlow+Semi+Condensed:wght@500;600&display=swap">
<style>
  :root {
    --parchment-light: #f6e6d6;
    --parchment-mid: #dcb48a;
    --parchment-dark: #b98250;
    --sepia-deep: #8a5530;
    --ink: #1a110a;
    --ink-soft: #2b1d12;
    --label-white: #fdf9f9;
  }
  * { margin: 0; padding: 0; box-sizing: border-box; }
  html, body { width: 1200px; height: 915px; overflow: hidden; background: var(--parchment-light); }
  .cover-wrap {
    position: relative;
    width: 1200px;
    height: 915px;
    overflow: hidden;
    background:
      radial-gradient(ellipse 700px 420px at 20% 95%, var(--parchment-light) 0%, rgba(246,230,214,0) 75%),
      radial-gradient(ellipse 500px 300px at 95% 5%, rgba(150,95,50,.45) 0%, rgba(150,95,50,0) 80%),
      linear-gradient(170deg, #c89465 0%, var(--parchment-mid) 35%, #e7c7a6 65%, var(--parchment-light) 100%);
    color: var(--ink);
  }

  /* Back cover */
  .back-blurb {
    position: absolute;
    left: 56px;
    top: 62px;
    width: 467px;
    font-family: "EB Garamond", serif;
    font-size: 17.4px;
    line-height: 30.8px;
    color: var(--ink-soft);
    text-align: justify;
  }
  .back-blurb p + p { margin-top: 30.8px; }
  .isbn-label {
    position: absolute;
    left: 316px;
    top: 738px;
    width: 220px;
    height: 133px;
    background: var(--label-white);
  }

  /* Spine */
  .spine-title, .spine-author {
    position: absolute;
    white-space: nowrap;
    transform-origin: left top;
    transform: rotate(-90deg);
  }
  .spine-title {
    left: 584px;
    top: 535px;
    font-family: "Playfair Display", serif;
    font-size: 17px;
    color: var(--ink);
  }
  .spine-author {
    left: 580px;
    top: 872px;
    font-family: "Barlow Semi Condensed", sans-serif;
    font-weight: 500;
    font-size: 21px;
    letter-spacing: 1.5px;
    color: var(--ink);
  }

  /* Front imagery */
  .portrait-area {
    position: absolute;
    left: 612px;
    top: 236px;
    width: 225px;
    height: 500px;
    background: radial-gradient(ellipse 50% 50% at 50% 45%, rgba(120,72,38,.55) 0%, rgba(150,95,55,.3) 55%, rgba(200,150,105,0) 100%);
  }
  .castle-area {
    position: absolute;
    left: 630px;
    top: 580px;
    width: 520px;
    height: 300px;
    background:
      radial-gradient(ellipse 60% 55% at 50% 55%, rgba(180,120,75,.55) 0%, rgba(205,150,105,.35) 60%, rgba(230,200,170,0) 100%),
      radial-gradient(ellipse 25% 50% at 100% 50%, rgba(120,65,30,.45) 0%, rgba(120,65,30,0) 100%);
  }

  /* Front title */
  .front-title { font-family: "Playfair Display", serif; color: var(--ink); }
  .front-title span {
    position: absolute;
    white-space: nowrap;
    line-height: 1;
    transform-origin: left top;
  }
  .title-das { left: 655px; top: 72px; font-size: 36px; font-weight: 700; transform: scaleX(.85); }
  .title-main { left: 658px; top: 106px; font-size: 104px; font-weight: 700; letter-spacing: -2px; transform: scaleX(.76); }
  .title-von { left: 777px; top: 248px; font-size: 36px; font-weight: 400; transform: scaleX(.85); }
  .title-schloss { left: 824px; top: 232px; font-size: 124px; font-weight: 400; letter-spacing: -2px; transform: scaleX(.78); }
  .title-city { left: 672px; top: 388px; font-size: 124px; font-weight: 400; letter-spacing: -2px; transform: scaleX(.78); }
  .genre-line {
    position: absolute;
    left: 917px;
    top: 519px;
    font-family: "Barlow Semi Condensed", sans-serif;
    font-weight: 600;
    font-size: 17px;
    letter-spacing: .4px;
    color: var(--ink);
  }
  .front-author {
    position: absolute;
    left: 746px;
    top: 835px;
    font-family: "Barlow Semi Condensed", sans-serif;
    font-weight: 500;
    font-size: 45px;
    letter-spacing: 3px;
    line-height: 1;
    color: var(--ink);
  }
</style>
</head>
<body>
<main class="cover-wrap">
  <section class="back-cover">
    <div class="back-blurb">
      <p>Lorem ipsum dolor sit amet, consetetur sadipscing elitr, sed diam nonumy eirmod tempor invidunt ut labore et dolore magna aliquyam erat, sed diam voluptua. At vero eos et accusam et justo duo dolores et ea rebum. Stet clita kasd gubergren, no sea takimata sanctus est Lorem ipsum dolor sit amet. Lorem ipsum dolor sit amet, consetetur sadipscing elitr, sed diam nonumy eirmod tempor invidunt ut labore et dolore magna aliquyam erat, sed diam voluptua.</p>
      <p>At vero eos et accusam et justo duo dolores et ea rebum. Stet clita kasd gubergren, no sea takimata sanctus est Lorem ipsum dolor sit amet. Lorem ipsum dolor sit amet, consetetur sadipscing elitr, sed diam nonumy eirmod tempor invidunt ut labore et dolore magna aliquyam erat, sed diam voluptua. At vero eos et accusam et justo duo dolores et ea rebum. Stet clita kasd gubergren, no sea takimata sanctus est Lorem ipsum dolor sit amet.</p>
    </div>
    <div class="isbn-label"></div>
  </section>

  <section class="spine">
    <div class="spine-title">Das Tödliche Erbe von Schloss Rothenburg</div>
    <div class="spine-author">AUTORENNAME</div>
  </section>

  <section class="front-cover">
    <div class="portrait-area" role="img" aria-label="Sepiafoto einer Frau im Profil mit hochgestecktem Haar und Spitzenkleid"></div>
    <div class="castle-area" role="img" aria-label="Sepiafoto eines historischen Torhauses mit Türmen und Fachwerk"></div>
    <h1 class="front-title">
      <span class="title-das">Das</span>
      <span class="title-main">Tödliche Erbe</span>
      <span class="title-von">von</span>
      <span class="title-schloss">Schloss</span>
      <span class="title-city">Rothenburg</span>
    </h1>
    <div class="genre-line">HISTORISCHER ROMAN</div>
    <div class="front-author">AUTORENNAME</div>
  </section>
</main>
</body>
</html>
```